Business card for a shipping supplies business

Needing a business card design. Please see the logo. The logo with the white font should be used if there is a dark background.

We are looking for the following info on the card. Please see the sample info. We will need the info to be changed with a few different employee names and info but all will use the same template.

Business Name: The Crate Heron
Employee Name : Marcus Delaney
Position: Account Manager
Address: 4827 W. Ridge 418 S.
Cedar Hollow, OK 73948
email: Marcus@thecrateheron.example
telephone: 855-619-2740 x 207
website: www.getparcelkits.example

Target Market(s)

Businesses who ship products for online sales

Industry/Entity Type

Cardboard

Contact Information for Business Card

Name, title, address, website, logo, telephone number

Font styles to use
Sans Serif

Colors
EE7325
F08F49
F5BC92
FAE3D3
FDF4ED

Requirements
Must have
• Logo on back of card. Clean look, just logo, website address

```html
<!DOCTYPE html>
<html lang="en">
<head>
<meta charset="utf-8">
<title>The Crate Heron – Business Card</title>
<link href="https://fonts.googleapis.com/css2?family=Jost:wght@400;500;600&display=swap" rel="stylesheet">
<style>
  :root{
    --navy:#031722;
    --orange:#ee7325;
    --rust:#d0582a;
    --tan:#c28b66;
    --ink:#1c1c1c;
    --paper:#ffffff;
    --stage:#f1f1f1;
    --edge:#9a9a9a;
  }
  *{margin:0;padding:0;box-sizing:border-box}
  html,body{width:1200px;height:1200px;overflow:hidden}
  body{background:var(--stage);font-family:"Jost",sans-serif;position:relative}

  .card{position:absolute;top:457px;width:500px;height:285px;overflow:hidden}

  /* Back of card */
  .card-back{left:80px;background:var(--navy)}
  .card-back .mark{position:absolute;left:50%;top:42px;width:86px;height:86px;margin-left:-43px;border-radius:50%;background:var(--orange)}
  .card-back .brand{position:absolute;left:0;right:0;top:140px;text-align:center;color:var(--paper);font-weight:600;font-size:32px;letter-spacing:1px;text-transform:uppercase;white-space:nowrap}
  .card-back .band{position:absolute;top:215px;height:29px;background:var(--orange)}
  .card-back .band-left{left:0;width:86px}
  .card-back .band-right{right:0;width:87px}
  .card-back .web{position:absolute;left:86px;right:87px;top:212px;text-align:center;color:var(--orange);font-size:22px;line-height:32px;white-space:nowrap}

  /* Front of card */
  .card-front{left:625px;background:var(--paper);border:1px solid var(--edge)}
  .card-front .side-band{position:absolute;left:0;top:0;width:149px;height:100%;background:var(--tan)}
  .card-front .mascot-art{position:absolute;left:0;top:0;width:190px;height:210px;border-radius:0 0 90px 0;background:linear-gradient(160deg,var(--rust) 0%,var(--rust) 55%,var(--ink) 100%)}
  .card-front .mark{position:absolute;left:200px;top:28px;width:62px;height:62px;border-radius:50%;background:var(--orange)}
  .card-front .brand{position:absolute;left:280px;top:45px;color:var(--rust);font-weight:600;font-size:21px;text-transform:uppercase;letter-spacing:.3px;white-space:nowrap}
  .card-front .person{position:absolute;left:200px;top:110px;font-size:16px;color:var(--ink);white-space:nowrap}
  .card-front .person .name{font-weight:600}
  .card-front .person .divider{color:var(--orange);margin:0 5px}
  .contact{position:absolute;left:200px;top:154px;list-style:none;font-size:14.5px;color:var(--ink);line-height:19px;white-space:nowrap}
  .contact li{display:flex;align-items:flex-start;margin-bottom:5px}
  .contact svg{flex:none;width:15px;height:15px;margin:2px 7px 0 0}
</style>
</head>
<body>

<section class="card card-back" aria-label="Card back">
  <div class="mark"></div>
  <div class="brand">The Crate Heron</div>
  <div class="band band-left"></div>
  <div class="web">www.getparcelkits.example</div>
  <div class="band band-right"></div>
</section>

<section class="card card-front" aria-label="Card front">
  <div class="side-band"></div>
  <div class="mascot-art" role="img" aria-label="Large mascot illustration in rust orange, black and white"></div>
  <div class="mark"></div>
  <div class="brand">The Crate Heron</div>
  <p class="person"><span class="name">Marcus Delaney</span><span class="divider">|</span><span class="title">Account Manager</span></p>
  <ul class="contact">
    <li>
      <svg viewBox="0 0 16 16"><path d="M8 1a5 5 0 0 0-5 5c0 4 5 9 5 9s5-5 5-9a5 5 0 0 0-5-5z" fill="#ee7325"/><circle cx="8" cy="6" r="2" fill="#fff"/></svg>
      <span>4827 W. Ridge 418 S.<br>Cedar Hollow, OK 73948</span>
    </li>
    <li>
      <svg viewBox="0 0 16 16"><circle cx="8" cy="8" r="8" fill="#ee7325"/><rect x="4" y="5" width="8" height="6" fill="none" stroke="#fff" stroke-width="1.2"/><path d="M4 5l4 3.5L12 5" fill="none" stroke="#fff" stroke-width="1.2"/></svg>
      <span>Marcus@thecrateheron.example</span>
    </li>
    <li>
      <svg viewBox="0 0 16 16"><circle cx="8" cy="8" r="8" fill="#ee7325"/><path d="M5 4l2 0 .8 2-1.2 1a5 5 0 0 0 2.4 2.4l1-1.2 2 .8 0 2c-4 0-7-3-7-7z" fill="#fff"/></svg>
      <span>855-619-2740 x 207</span>
    </li>
    <li>
      <svg viewBox="0 0 16 16"><circle cx="8" cy="8" r="8" fill="#ee7325"/><circle cx="8" cy="8" r="4.5" fill="none" stroke="#fff" stroke-width="1"/><path d="M3.5 8h9M8 3.5c-2 2.5-2 6.5 0 9M8 3.5c2 2.5 2 6.5 0 9" fill="none" stroke="#fff" stroke-width="1"/></svg>
      <span>www.getparcelkits.example</span>
    </li>
  </ul>
</section>

</body>
</html>
```